BOLD & MINIMALIST DESIGN NEEDED

We want a very bold but minimalistic business card design that is impactful and utilizes both sides of the business card. Our current logo is included for your use.

We want bold fonts and good use of negative space. We don't want the logo to overpower the design.

Target Market(s)

Professionals who are building new commercial buildings.

Industry/Entity Type

Construction

Contact Information for Business Card

Name, Title, email, office phone, cell phone, website

Font styles to use
Serif
Sans Serif

Requirements
Must have
• Bold design!

```html
<!DOCTYPE html>
<html lang="en">
<head>
<meta charset="utf-8">
<title>Ridgeline Works – Business Card</title>
<link rel="stylesheet" href="https://fonts.googleapis.com/css2?family=Montserrat:wght@400;500;800&display=swap">
<style>
  :root {
    --bg-dark: #3a3a3a;
    --bg-light: #5a5a5a;
    --paper: #f4f4f2;
    --ink: #111111;
    --night: #161616;
    --lime: #6cbf2a;
    --white: #f2f2f2;
  }
  * { margin: 0; padding: 0; box-sizing: border-box; }
  html, body { width: 1200px; height: 1050px; overflow: hidden; }
  body {
    background: linear-gradient(135deg, var(--bg-dark), var(--bg-light));
    font-family: "Montserrat", Arial, sans-serif;
    position: relative;
  }
  .card {
    position: absolute;
    left: 220px;
    width: 760px;
    height: 440px;
    border-bottom: 8px solid var(--lime);
    box-shadow: 0 24px 50px rgba(0,0,0,0.45);
  }
  .card--front { top: 60px; background: var(--paper); color: var(--ink); }
  .card--back { top: 550px; background: var(--night); color: var(--white); }

  .brand {
    display: flex;
    align-items: center;
    gap: 14px;
    font-weight: 800;
    letter-spacing: 0.5px;
  }
  .brand__mark { width: 22px; height: 22px; background: var(--lime); }
  .card--front .brand { position: absolute; left: 56px; top: 52px; font-size: 40px; }

  .contact {
    position: absolute;
    left: 410px;
    top: 150px;
    line-height: 1.45;
  }
  .contact__name { font-weight: 800; font-size: 34px; letter-spacing: 0.5px; }
  .contact__title { font-size: 18px; font-weight: 500; margin-bottom: 18px; }
  .contact__address { font-size: 16px; margin-bottom: 14px; }
  .contact__list { list-style: none; font-size: 16px; }
  .contact__list li { display: flex; align-items: center; gap: 10px; margin-bottom: 4px; }
  .contact__list svg { width: 16px; height: 16px; fill: var(--lime); flex: none; }

  .card--back .brand {
    position: absolute;
    inset: 0;
    justify-content: center;
    font-size: 56px;
  }
  .card--back .brand__mark { width: 30px; height: 30px; }
</style>
</head>
<body>
  <section class="card card--front">
    <div class="brand"><span class="brand__mark"></span>RIDGELINE WORKS</div>
    <div class="contact">
      <p class="contact__name">MAREK OLSEN</p>
      <p class="contact__title">Director</p>
      <p class="contact__address">Birkenallee 12,<br>30000 Nordstadt</p>
      <ul class="contact__list">
        <li>
          <svg viewBox="0 0 24 24" aria-hidden="true"><path d="M6.6 10.8a15.1 15.1 0 0 0 6.6 6.6l2.2-2.2a1 1 0 0 1 1-.25 11.4 11.4 0 0 0 3.6.57 1 1 0 0 1 1 1V20a1 1 0 0 1-1 1A17 17 0 0 1 3 4a1 1 0 0 1 1-1h3.5a1 1 0 0 1 1 1c0 1.25.2 2.45.57 3.6a1 1 0 0 1-.25 1z"/></svg>
          0160 5550142
        </li>
        <li>
          <svg viewBox="0 0 24 24" aria-hidden="true"><path d="M2 5h20v14H2zm2 2v.5l8 5 8-5V7zm0 2.9V17h16V9.9l-8 5z"/></svg>
          info@ridgelineworks.com
        </li>
        <li>
          <svg viewBox="0 0 24 24" aria-hidden="true"><path d="M12 2a10 10 0 1 0 0 20 10 10 0 0 0 0-20zm6.9 9h-3a15 15 0 0 0-1.3-5.5A8 8 0 0 1 18.9 11zM12 4.1c.9 1.3 1.7 3.7 1.9 6.9h-3.8c.2-3.2 1-5.6 1.9-6.9zM9.4 5.5A15 15 0 0 0 8.1 11h-3a8 8 0 0 1 4.3-5.5zM5.1 13h3a15 15 0 0 0 1.3 5.5A8 8 0 0 1 5.1 13zm6.9 6.9c-.9-1.3-1.7-3.7-1.9-6.9h3.8c-.2 3.2-1 5.6-1.9 6.9zm2.6-1.4a15 15 0 0 0 1.3-5.5h3a8 8 0 0 1-4.3 5.5z"/></svg>
          www.ridgelineworks.com
        </li>
      </ul>
    </div>
  </section>

  <section class="card card--back">
    <div class="brand"><span class="brand__mark"></span>RIDGELINE WORKS</div>
  </section>
</body>
</html>
```